Digital Member Badge Designs for Online Membership Directory

Atomic Lounge Revival Collective Today

I need three or four Member Badges for my online member directory.

Website: https://www.brv44k.com/

1) Founding Member
2) Individual Member
3) Business Member

I have attached a sample of the required dimensions.
In addition, here are some examples from Findqora Picture Lookup: https://www.findqora.com.au/search?q=online%20membership%20directory%20member%20badges

Target Market(s)

Mid century modern design enthusiasts

Requirements
Must have
• Mid century modern design and include the words, Founding Member
Nice to have
• See my website design for inspiration: www.brv44k.com

```html
<!DOCTYPE html>
<html lang="en">
<head>
<meta charset="utf-8">
<title>Member Plans</title>
<link rel="stylesheet" href="https://fonts.googleapis.com/css2?family=Quicksand:wght@400;500;600;700&family=Figtree:wght@400;600;700&display=swap">
<style>
  :root {
    --page-bg: #dde9ea;
    --card-bg: #e7f6f6;
    --ink: #1d1d24;
    --ink-soft: #2b2b33;
    --founding: #9b1b4a;
    --founding-teal: #3a8a7a;
    --individual: #5a0f8a;
    --individual-blue: #5aaad6;
    --business: #d65060;
    --business-navy: #2c3262;
  }
  * { margin: 0; padding: 0; box-sizing: border-box; }
  html, body { width: 1200px; height: 831px; overflow: hidden; }
  body { background: var(--page-bg); color: var(--ink); font-family: "Quicksand", sans-serif; position: relative; }

  .plan-card {
    position: absolute; left: 60px; width: 266px; height: 211px;
    background: var(--card-bg); border-radius: 32px;
    text-align: center; font-family: "Figtree", sans-serif;
  }
  .plan-card--founding { top: 57px; }
  .plan-card--individual { top: 312px; left: 62px; }
  .plan-card--business { top: 567px; }

  .plan-badge { position: absolute; border-radius: 46% 54% 44% 56% / 52% 46% 54% 48%; }
  .plan-badge--founding {
    left: 65px; top: 17px; width: 134px; height: 98px;
    background: radial-gradient(ellipse at 50% 45%, #ffffff 0%, #ffffff 38%, rgba(155,27,74,.55) 72%, rgba(58,138,122,.55) 100%);
  }
  .plan-badge--individual {
    left: 76px; top: 17px; width: 118px; height: 91px;
    background: radial-gradient(ellipse at 50% 45%, #ffffff 0%, #ffffff 38%, rgba(90,15,138,.5) 72%, rgba(90,170,214,.55) 100%);
  }
  .plan-badge--business {
    left: 88px; top: 20px; width: 90px; height: 92px;
    background: radial-gradient(ellipse at 50% 45%, #ffffff 0%, #ffffff 38%, rgba(214,80,96,.55) 72%, rgba(44,50,98,.5) 100%);
  }

  .plan-name { position: absolute; left: 0; right: 0; top: 120px; font-size: 13.5px; font-weight: 700; color: #111; }
  .plan-price { position: absolute; left: 0; right: 0; top: 139px; font-size: 10.5px; color: #111; }
  .plan-select {
    position: absolute; left: 50%; top: 168px; transform: translateX(-50%);
    width: 77px; height: 24px; border-radius: 12px; color: #fff;
    font-size: 9px; line-height: 24px; letter-spacing: .2px;
  }
  .plan-select--founding { background: var(--founding); }
  .plan-select--individual { background: var(--individual); }
  .plan-select--business { background: var(--business); }

  .plan-detail { position: absolute; }
  .plan-detail--founding { left: 407px; top: 57px; }
  .plan-detail--individual { left: 400px; top: 324px; }
  .plan-detail--business { left: 402px; top: 569px; }

  .plan-note { font-size: 12px; font-weight: 600; color: var(--ink-soft); white-space: nowrap; }
  .plan-detail--individual .plan-note, .plan-detail--business .plan-note { font-size: 11.6px; }
  .plan-intro { color: var(--ink-soft); white-space: nowrap; }
  .plan-detail--founding .plan-intro { font-size: 16.2px; line-height: 24.2px; margin-top: 10px; }
  .plan-detail--individual .plan-intro { font-size: 15px; line-height: 22.5px; margin-top: 10px; }
  .plan-detail--business .plan-intro { font-size: 15.6px; line-height: 23.5px; margin-top: 10px; }
  .plan-intro strong { font-weight: 700; color: var(--ink); }

  .plan-features { list-style: none; display: grid; grid-auto-flow: column; grid-template-rows: repeat(3, auto); position: absolute; white-space: nowrap; font-weight: 600; color: var(--ink); }
  .plan-features li { position: relative; }
  .plan-features li::before { content: "•"; position: absolute; left: -13px; font-size: .8em; }
  .plan-detail--founding .plan-features { top: 108px; left: 36px; font-size: 16.2px; line-height: 32.3px; grid-template-columns: 345px auto; }
  .plan-detail--individual .plan-features { top: 101px; left: 33px; font-size: 15px; line-height: 30px; grid-template-columns: 320px auto; }
  .plan-detail--business .plan-features { top: 106px; left: 34px; font-size: 15.6px; line-height: 31.2px; grid-template-columns: 325px auto; }
</style>
</head>
<body>
  <section class="plan-card plan-card--founding">
    <div class="plan-badge plan-badge--founding" role="img" aria-label="Founding Member badge: retro lettering with floor lamp, starburst and lounge chair in crimson and teal"></div>
    <h2 class="plan-name">Founding Member</h2>
    <p class="plan-price">$18/twice a year</p>
    <div class="plan-select plan-select--founding">SELECT PLAN</div>
  </section>
  <div class="plan-detail plan-detail--founding">
    <p class="plan-note">[Limited to the first 1,000 members only and not transferable]</p>
    <p class="plan-intro"><strong>Founding Member</strong>, have a say in the direction of the community and the types of content<br>and features that are developed. Your feedback, suggestions and ideas can help shape the<br>community's culture and growth. Join me now and I'll see you on the other side!</p>
    <ul class="plan-features">
      <li>Priority Listing in Directory</li><li>List in 10 Categories</li><li>Post Classifieds</li>
      <li>Post Community Articles</li><li>Discussions Enabled</li><li>Private Chat Enabled</li>
    </ul>
  </div>

  <section class="plan-card plan-card--individual">
    <div class="plan-badge plan-badge--individual" role="img" aria-label="Individual member badge: retro lettering with lounge chair, pendant lamp, starbursts and oval rug in purple and sky blue"></div>
    <h2 class="plan-name">Individual</h2>
    <p class="plan-price">$18/twice a year</p>
    <div class="plan-select plan-select--individual">SELECT PLAN</div>
  </section>
  <div class="plan-detail plan-detail--individual">
    <p class="plan-note">[The Individual plan will become available once the allocation of the Founding Member plan is exhausted]</p>
    <p class="plan-intro">Our member directory can help you connect with other individuals and organisations who<br>are interested in mid century modern design. The directory also offers access to resources<br>and opportunities for community building. Join us for some fun and adventure.</p>
    <ul class="plan-features">
      <li>Listing in Member Directory</li><li>List in 5 Categories</li><li>View Classifieds</li>
      <li>View Community Articles</li><li>Discussions Enabled</li><li>Private Chat Enabled</li>
    </ul>
  </div>

  <section class="plan-card plan-card--business">
    <div class="plan-badge plan-badge--business" role="img" aria-label="Business member badge: retro lettering with sideboard, lamps and starburst in coral and navy"></div>
    <h2 class="plan-name">Business</h2>
    <p class="plan-price">$18/twice a year</p>
    <div class="plan-select plan-select--business">SELECT PLAN</div>
  </section>
  <div class="plan-detail plan-detail--business">
    <p class="plan-note">[The Business plan will become available once the allocation of the Founding Member plan is exhausted]</p>
    <p class="plan-intro">Our member directory can help with increased visibility, enhance your credibility and<br>reputation, and nurture business growth. The directory is great way to expand your<br>business network, gain access to resources, and open up new opportunities. Join today!</p>
    <ul class="plan-features">
      <li>Listing in Member Directory</li><li>List in 10 Categories</li><li>Post Classifieds</li>
      <li>Post Community Articles</li><li>Discussions Enabled</li><li>Private Chat Enabled</li>
    </ul>
  </div>
</body>
</html>
```